Pharmacy window design

WINDOW DIMENSIONS

4ft 8 1/2" WIDE
7ft 4 1/2" HIGH

i need a window sticker for 4 windows for the outside of a pharmacy. see attached examples. name of the pharmacy is Vita Corner

we would prefer to display products on the window signs eg. Baby care products, medicines. vitamins. fitness. veterinary, Health/ beauty etc.

Target Market(s)

Locals and Tourists

Industry/Entity Type

Pharmacy

```html
<!DOCTYPE html>
<html lang="en">
<head>
<meta charset="utf-8">
<title>Vita Corner Pharmacy – Window Sign</title>
<link href="https://fonts.googleapis.com/css2?family=Oswald:wght@500;700&family=Poppins:wght@600&display=swap" rel="stylesheet">
<style>
  :root {
    --blue: #2f4a9c;
    --green: #6cc04a;
    --green-soft: #a9dc8f;
    --white: #ffffff;
  }
  * { margin: 0; padding: 0; box-sizing: border-box; }
  html, body { width: 756px; height: 1200px; overflow: hidden; background: var(--white); }
  .sign { position: relative; width: 756px; height: 1200px; background: var(--white); font-family: 'Oswald', sans-serif; }
  .backdrop { position: absolute; inset: 0; }
  .brand { position: absolute; top: 52px; left: 0; width: 100%; display: flex; justify-content: center; align-items: center; gap: 14px; }
  .brand-dot { width: 22px; height: 22px; background: var(--green); }
  .brand-text { font-family: 'Poppins', sans-serif; font-weight: 600; color: var(--green); line-height: 1; text-align: center; }
  .brand-name { font-size: 54px; }
  .brand-sub { font-size: 22px; letter-spacing: 4px; margin-top: 6px; }
  .headline { position: absolute; top: 596px; width: 100%; text-align: center; color: var(--blue); font-weight: 700; font-size: 104px; line-height: 1; letter-spacing: 1px; }
  .range-band { position: absolute; top: 718px; left: 20px; right: 20px; height: 58px; background: var(--green); color: var(--white); font-weight: 700; font-size: 43px; line-height: 58px; text-align: center; }
  .range-line { position: absolute; top: 784px; width: 100%; text-align: center; color: var(--blue); font-weight: 700; font-size: 38px; line-height: 1.2; }
  .rule { position: absolute; left: 20px; right: 20px; height: 5px; background: var(--green); }
  .rule-top { top: 842px; }
  .rule-bottom { top: 1062px; }
  .categories { position: absolute; top: 868px; left: 30px; right: 30px; display: flex; justify-content: space-between; }
  .category { width: 160px; text-align: center; }
  .category svg { display: block; margin: 0 auto; }
  .category-label { margin-top: 10px; color: var(--green); font-weight: 700; font-size: 22px; }
  .call { position: absolute; top: 1074px; width: 100%; text-align: center; color: var(--blue); font-weight: 700; font-size: 62px; line-height: 90px; letter-spacing: 1px; }
  .foot-band { position: absolute; bottom: 0; left: 0; right: 0; height: 26px; background: var(--blue); }
</style>
</head>
<body>
<div class="sign">
  <svg class="backdrop" width="756" height="1200" viewBox="0 0 756 1200">
    <polygon points="0,0 200,0 0,210" fill="var(--blue)"/>
    <polygon points="756,0 556,0 756,210" fill="var(--blue)"/>
    <polygon points="0,250 130,420 0,590" fill="var(--blue)"/>
    <polygon points="756,250 626,420 756,590" fill="var(--blue)"/>
    <polygon points="268,210 488,210 600,395 488,580 268,580 156,395" fill="none" stroke="var(--green)" stroke-width="16"/>
    <polygon points="280,232 476,232 572,395 476,558 280,558 184,395" fill="var(--green-soft)" role="img" aria-label="Family with a pet held in caring open hands illustration"/>
  </svg>

  <div class="brand">
    <span class="brand-dot"></span>
    <div class="brand-text">
      <div class="brand-name">Vita Corner</div>
      <div class="brand-sub">PHARMACY</div>
    </div>
  </div>

  <h1 class="headline">CARE ABOUT FOR</h1>
  <div class="range-band">HEALTH &amp; BEAUTY, BABY CARE,</div>
  <div class="range-line">VETERINARY &amp; FITNESS, VITAMINS &amp; MEDICINES</div>
  <div class="rule rule-top"></div>

  <div class="categories">
    <div class="category">
      <svg width="140" height="124" viewBox="0 0 140 124">
        <polygon points="38,4 102,4 136,62 102,120 38,120 4,62" fill="none" stroke="var(--blue)" stroke-width="7"/>
        <g transform="rotate(-40 70 62)">
          <rect x="36" y="46" width="68" height="32" rx="16" fill="var(--white)" stroke="var(--blue)" stroke-width="6"/>
          <path d="M70 46 h18 a16 16 0 0 1 0 32 h-18 z" fill="var(--blue)"/>
        </g>
      </svg>
      <div class="category-label">MEDICINES</div>
    </div>
    <div class="category">
      <svg width="140" height="124" viewBox="0 0 140 124">
        <polygon points="38,4 102,4 136,62 102,120 38,120 4,62" fill="none" stroke="var(--blue)" stroke-width="7"/>
        <rect x="52" y="26" width="36" height="12" fill="var(--blue)"/>
        <rect x="46" y="40" width="48" height="60" rx="6" fill="var(--blue)"/>
        <rect x="52" y="58" width="36" height="22" fill="var(--white)"/>
      </svg>
      <div class="category-label">VITAMINS</div>
    </div>
    <div class="category">
      <svg width="140" height="124" viewBox="0 0 140 124">
        <polygon points="38,4 102,4 136,62 102,120 38,120 4,62" fill="none" stroke="var(--blue)" stroke-width="7"/>
        <rect x="36" y="30" width="68" height="64" rx="10" fill="var(--blue)" opacity="0.85" role="img" aria-label="Person running on a treadmill icon"/>
      </svg>
      <div class="category-label">FITNESS</div>
    </div>
    <div class="category">
      <svg width="140" height="124" viewBox="0 0 140 124">
        <polygon points="38,4 102,4 136,62 102,120 38,120 4,62" fill="none" stroke="var(--blue)" stroke-width="7"/>
        <rect x="36" y="30" width="68" height="64" rx="10" fill="var(--blue)" opacity="0.85" role="img" aria-label="Veterinarian icon"/>
      </svg>
      <div class="category-label">VETERINARY</div>
    </div>
  </div>

  <div class="rule rule-bottom"></div>
  <div class="call">CALL NOW - 555 010 246</div>
  <div class="foot-band"></div>
</div>
</body>
</html>
```